Marine & Offshore company business card

We need a new logo design for a new company based in Singapore called "Venmoor Global Pte. Ltd.". We are suppliers of electrical items to marine and offshore industry. We specialise in lightings, cables terminations and junction box customisation. We would like the name card to have simple modern classic look.

Target Market(s)

my target customers are ship owners, shipyard purchasers, offshore purchasers.

Industry/Entity Type

Electrical

Font styles to use
Serif
Sans Serif

Colors

Designer to choose colors to be used in the design.

```html
<!DOCTYPE html>
<html lang="en">
<head>
<meta charset="utf-8">
<title>Venmoor Global Pte. Ltd. – Business Card</title>
<link href="https://fonts.googleapis.com/css2?family=Mulish:wght@400;500;700&display=swap" rel="stylesheet">
<style>
  :root{
    --stage:#2b2b2d;
    --navy:#1b2630;
    --gold:#c99a21;
    --white:#ffffff;
    --ink:#1e2a33;
    --paper:#ffffff;
  }
  *{box-sizing:border-box;margin:0;padding:0}
  html,body{width:1200px;height:900px;overflow:hidden}
  body{background:var(--stage);font-family:"Mulish",sans-serif;position:relative}
  .card{position:absolute;top:302px;width:514px;height:296px;overflow:hidden;box-shadow:0 3px 10px rgba(0,0,0,.45)}
  .card--front{left:72px;background:var(--navy);color:var(--white)}
  .card--back{left:615px;background:var(--paper);color:var(--ink)}

  .tagline{position:absolute;left:38px;top:38px;font-size:15px;line-height:23px;font-weight:400}
  .wordmark{position:absolute;font-weight:700;letter-spacing:.3px;line-height:1.1}
  .card--front .wordmark{left:38px;top:222px;width:220px;font-size:22px;color:var(--white)}
  .card--back .wordmark{left:38px;top:80px;white-space:nowrap;font-size:21px;color:var(--ink)}

  .person{position:absolute;left:96px;top:138px}
  .person__name{font-size:17px;color:var(--gold);font-weight:500}
  .person__role{font-size:13px;margin-top:3px}

  .contacts{position:absolute;left:96px;top:186px;list-style:none;font-size:13px;line-height:16px}
  .contacts li{display:flex;align-items:center;gap:5px;white-space:nowrap}
  .contacts svg{width:11px;height:11px;fill:var(--gold)}

  .address{position:absolute;left:320px;top:210px;font-size:13px;line-height:16px;white-space:nowrap}

  .wave{position:absolute;left:0;bottom:0;width:514px;height:60px}
</style>
</head>
<body>
  <section class="card card--front">
    <p class="tagline">We specialise in lightings,<br>cables terminations and<br>junction box customisation</p>
    <p class="wordmark">Venmoor Global Pte. Ltd.</p>
  </section>

  <section class="card card--back">
    <p class="wordmark">Venmoor Global Pte. Ltd.</p>
    <div class="person">
      <p class="person__name">Daniel Harcourt</p>
      <p class="person__role">managing director</p>
    </div>
    <ul class="contacts">
      <li><svg viewBox="0 0 12 12"><path d="M2.5 1l2 2.5-1 1.3c.7 1.4 1.8 2.5 3.2 3.2l1.3-1 2.5 2-1 1.8C5.5 11 1 6.5.8 2z"/></svg>654 210 37 19</li>
      <li><svg viewBox="0 0 12 12"><path d="M3 0h6v12H3zM4 1.5v8h4v-8z"/></svg>912 480 63 27</li>
      <li><svg viewBox="0 0 12 12"><path d="M3 0h6v3H3zM1 4h10v5H9v3H3V9H1zM4 8v3h4V8z"/></svg>654 210 37 20</li>
      <li><svg viewBox="0 0 12 12"><path d="M0 2h12v8H0zM1 3l5 3.5L11 3z" fill-rule="evenodd"/></svg>dharcourt@venmoor-gl.com</li>
    </ul>
    <div class="address">
      <p>48 Keppel Quay Road</p>
      <p>Keppel, Singapore 098765</p>
      <p>www.venmoor-gl.com</p>
    </div>
    <svg class="wave" viewBox="0 0 514 60" preserveAspectRatio="none" aria-hidden="true">
      <path d="M0 60V52C110 38 220 40 320 44 410 47 470 34 514 18V60z" fill="var(--navy)"/>
      <path d="M0 54C90 36 200 34 320 43 210 38 100 40 0 46z" fill="var(--gold)"/>
    </svg>
  </section>
</body>
</html>
```